Mortgage and Asset Finance Broker Needs a Wordpress Website Design

I need a modern looking Wordpress website to showcase my service as a mortgage and asset broker. I have a company and we work with various lenders to arrange mortgages, as well as commercial lending and business asset finance. The website needs to look professional, be easy to navigate and capture leads. SEO is obviously very important to me. It really needs to be something that shows trust and professioanlism.
Updates

On the home page I will need to have some boxes for Home Loans, Refinancing, Business (and Agriculture) Loans etc. I'd like a carousel in the middle which shows our lenders (so that can have the banks logos added).

It needs to be easy top navigate and showcase all we do - Home Loans, Refinancing, Commercial Loans, Car Loans, Asset Finance etc.

There are plenty of companies on the internet that do this.

There is some good information here https://lendquill.example.au/mortgage-broker-homepage/

I need to make sure that editing the website is easy (I think Wordpress has something that allows that).

Also we are very much an Australian business so that is something to advertise.

Industry/Entity Type

Mortgage and Finance Broker

Coding

Coded - Design and coding required

Number of Pages Required

5+ page

Requirements
Must have
• Easy to navigate professional feel. Must be responsive and mobile friendly.
Nice to have
• Homepage with links to inner pages. Contact buttons.

```html
<!DOCTYPE html>
<html lang="en">
<head>
<meta charset="utf-8">
<title>Vantora – Home Loans &amp; Business Finance</title>
<link rel="stylesheet" href="https://fonts.googleapis.com/css2?family=Poppins:wght@500;600;700;800&family=Jost:wght@400;500;600&display=swap">
<style>
:root{
  --blue:#0c4f96;
  --blue-dark:#0b3f7c;
  --navy:#0e2748;
  --orange:#f39a3a;
  --purple:#6b4189;
  --pink:#ee3e78;
  --pink-soft:#f7d3df;
  --ink:#1d1d1f;
  --muted:#444;
  --light:#f3f3f5;
  --white:#fff;
}
*{box-sizing:border-box;margin:0;padding:0}
html,body{width:1200px;height:3883px;overflow:hidden}
body{position:relative;font-family:"Jost",sans-serif;color:var(--ink);background:var(--white)}
.abs{position:absolute}
h1,h2,h3{font-family:"Poppins",sans-serif;font-weight:800}
.eyebrow{font-size:21px;color:var(--ink);display:flex;align-items:center;gap:16px}
.eyebrow::after{content:"";width:86px;height:3px;background:var(--orange)}
.eyebrow.light{color:#fff}
.btn{display:inline-flex;align-items:center;justify-content:center;background:var(--blue);color:#fff;font-size:21px;box-shadow:0 3px 0 #08356a}
.photo{border-radius:0}

/* header */
.site-header{left:0;top:0;width:1200px;height:146px;background:#fff}
.brand{left:113px;top:30px;font-family:"Poppins",sans-serif;font-weight:800;font-size:62px;color:var(--ink);display:flex;align-items:center;gap:14px;letter-spacing:-1px}
.brand .mark{width:34px;height:34px;background:var(--blue)}
.topbar{left:433px;top:0;width:767px;height:50px;background:var(--blue);border-bottom-left-radius:30px;color:#fff;font-size:15px;display:flex;align-items:center;gap:44px;padding-left:32px}
.topbar span{display:flex;align-items:center;gap:10px}
.nav{left:438px;top:88px;display:flex;align-items:center;font-size:16px;font-weight:500}
.nav a{color:var(--ink);text-decoration:none;margin-right:52px}
.nav .active{background:var(--purple);color:#fff;padding:4px 20px;border-radius:4px 16px 4px 4px;margin-right:44px}

/* hero */
.hero{left:0;top:146px;width:1200px;height:532px;background:linear-gradient(90deg,#050505 0%,#1a1a1a 30%,#6a5a52 60%,#b9b3ad 100%)}
.hero-copy{left:111px;top:112px;color:#fff}
.hero-copy p{font-size:17px;margin-bottom:18px}
.hero-copy h1{font-size:44px;line-height:52px;color:#fff}
.hero-copy h1 em{font-style:normal;color:var(--orange)}
.hero-btn{left:113px;top:338px;width:166px;height:42px}
.chip{top:457px;height:75px;width:205px;display:flex;align-items:center;gap:12px;padding:0 16px;font-family:"Poppins",sans-serif;font-weight:600;font-size:15px;line-height:22px;border-radius:8px 8px 0 0}
.chip.white{left:112px;background:#fff;color:var(--ink)}
.chip.purple{left:333px;background:var(--purple);color:#fff}

/* about */
.about{left:0;top:678px;width:1200px;height:486px;background:var(--light)}
.about .eyebrow{position:absolute;left:108px;top:68px}
.about h2{position:absolute;left:108px;top:108px;font-size:41px;line-height:56px;color:var(--blue)}
.about .lead{position:absolute;left:113px;top:234px;width:480px;font-size:17px;line-height:24px;color:var(--muted)}
.badge{position:absolute;top:344px;display:flex;gap:12px;align-items:center}
.badge .ring{width:64px;height:64px;border-radius:50%;background:var(--pink-soft);display:flex;align-items:center;justify-content:center}
.badge b{display:block;font-family:"Poppins",sans-serif;color:var(--blue);font-size:15px}
.badge small{display:block;font-size:10px;line-height:12px;color:#555;width:140px}
.about-frame{left:658px;top:60px;width:440px;height:335px;border:2px solid var(--orange);border-radius:18px;transform:rotate(-4deg)}
.about-photo{left:672px;top:73px;width:416px;height:332px;border-radius:14px;background:linear-gradient(135deg,#8a8378,#5c5448 60%,#3e372f)}

/* services */
.services{left:0;top:1164px;width:1200px;height:509px;background:var(--blue)}
.services .eyebrow{position:absolute;left:458px;top:72px}
.services h2{position:absolute;left:0;width:1200px;text-align:center;top:102px;font-size:40px;color:#fff}
.loan-card{top:1340px;width:312px;height:425px;background:#fff;box-shadow:0 4px 12px rgba(0,0,0,.12);text-align:center}
.loan-card .img{height:215px}
.loan-card h3{font-size:20px;font-weight:600;margin-top:26px}
.loan-card p{font-size:15px;line-height:21px;color:#333;margin:12px 22px 0}
.loan-card .btn{position:absolute;left:69px;top:362px;width:164px;height:43px}

/* features */
.know .eyebrow{position:absolute;left:463px;top:1845px}
.know h2{left:0;width:1200px;text-align:center;top:1878px;font-size:40px;line-height:56px;color:var(--blue)}
.feature{top:2011px;width:292px;height:87px;background:#fff;box-shadow:0 2px 10px rgba(0,0,0,.12);border-bottom:4px solid var(--blue);display:flex;align-items:center;gap:20px;padding-left:16px;font-family:"Poppins",sans-serif;font-weight:600;font-size:15px;line-height:22px}

/* trust */
.trust{left:0;top:2163px;width:1200px;height:451px;background:var(--blue)}
.trust .eyebrow{position:absolute;left:113px;top:76px}
.trust h2{position:absolute;left:112px;top:100px;font-size:39px;line-height:56px;color:#fff}
.checks{position:absolute;left:116px;top:278px;display:grid;grid-template-columns:172px 180px;row-gap:12px;color:#fff;font-size:17px}
.checks li{list-style:none;display:flex;align-items:center;gap:12px}
.steps{left:547px;top:2147px;width:541px;height:398px;background:var(--purple);border-radius:16px;border-top:8px solid #f0a7c3;padding:35px 40px}
.step{height:58px;background:#fff;border-radius:6px;margin-bottom:28px;display:flex;align-items:center;gap:22px;padding-left:14px;color:var(--blue);font-size:16px;line-height:26px}
.step .num{flex:none;width:34px;height:34px;border-radius:50%;background:var(--blue);color:#fff;font-family:"Poppins",sans-serif;font-weight:700;display:flex;align-items:center;justify-content:center}

/* why */
.why{left:0;top:2614px;width:1200px;height:602px;background:var(--light)}
.why-photo{left:112px;top:65px;width:477px;height:472px;background:linear-gradient(135deg,#d8d4cf,#8d8480 55%,#2a2a2e)}
.why .eyebrow{position:absolute;left:614px;top:62px}
.why h2{position:absolute;left:613px;top:92px;font-size:39px;color:var(--blue)}
.why .lead{position:absolute;left:612px;top:178px;width:480px;font-size:17px;line-height:24px;color:var(--muted)}
.why .badge{top:256px}
.why .badge b{font-size:16px;line-height:23px}
.bar{position:absolute;left:612px;width:462px}
.bar .label{font-size:20px;color:#222;display:flex;justify-content:space-between;align-items:flex-end}
.bar .label small{font-size:13px;margin-right:20px}
.bar .track{height:3px;background:#888;margin-top:8px}
.bar .fill{height:3px;background:var(--blue)}

/* cta */
.cta{left:0;top:3216px;width:1200px;height:281px;background:linear-gradient(90deg,#1e62ad,#2d74c0 50%,#1e62ad);text-align:center;color:#fff}
.cta p{margin-top:72px;font-size:25px}
.cta h2{margin-top:12px;font-size:40px;color:#fff}
.cta .btn{margin-top:18px;background:var(--pink);box-shadow:none;width:186px;height:42px}

/* footer */
.footer{left:0;top:3497px;width:1200px;height:386px;background:var(--navy);color:#fff}
.f-logo{position:absolute;left:111px;top:68px;width:192px;height:76px;background:#fff;display:flex;align-items:center;justify-content:center;gap:10px;font-family:"Poppins",sans-serif;font-weight:800;font-size:34px;color:var(--ink)}
.f-logo .mark{width:20px;height:20px;background:var(--blue)}
.f-about{position:absolute;left:111px;top:167px;width:270px;font-size:13px;line-height:24px}
.f-col h4{font-family:"Poppins",sans-serif;font-weight:600;font-size:16px;margin-bottom:22px}
.f-links li{list-style:none;font-size:13px;margin-bottom:14px;display:flex;align-items:center;gap:10px}
.news{display:flex;gap:10px;margin-bottom:16px;padding-bottom:10px;border-bottom:1px solid #4a5f80;width:246px}
.news .thumb{width:86px;height:60px;background:linear-gradient(135deg,#c7c0b5,#5a6a80)}
.news small{display:block;font-size:9px;color:#7fb3ff}
.news span{font-size:12px;line-height:21px}
.contact-item{display:flex;gap:12px;font-size:14px;line-height:23px;margin-bottom:10px}
.copyright{position:absolute;left:112px;top:337px;width:972px;border-top:1px solid #5a6d8a;text-align:center;padding-top:16px;font-size:14px}
</style>
</head>
<body>

<header class="abs site-header">
  <div class="abs brand"><span class="mark"></span>Vantora</div>
  <div class="abs topbar">
    <span>Login&nbsp;&nbsp;/&nbsp;&nbsp;Company News</span>
    <span><svg width="16" height="16" viewBox="0 0 24 24"><path d="M6 2l4 4-2 3c1 3 4 6 7 7l3-2 4 4-3 4C10 21 3 14 2 5z" fill="#fff"/></svg>(02) 5550 1846</span>
    <span><svg width="20" height="14" viewBox="0 0 20 14"><rect x="1" y="1" width="18" height="12" fill="none" stroke="#fff" stroke-width="2"/><path d="M1 1l9 7 9-7" fill="none" stroke="#fff" stroke-width="2"/></svg>Mon -Sat&nbsp; 8.00 am to 6.00pm</span>
  </div>
  <nav class="abs nav">
    <a class="active">Home</a><a>About</a><a>Services ⌄</a><a>News ⌄</a><a>Lenders</a><a>Contact Us</a>
  </nav>
</header>

<section class="abs hero" role="img" aria-label="Photo of a smiling loan adviser in a blazer meeting a client at a desk">
  <div class="abs hero-copy">
    <p>Welcome to Vantora</p>
    <h1>Helping Australians<br>Secure the <em>Right Loan</em>,<br>Every Time</h1>
  </div>
  <a class="abs btn hero-btn">Apply Loan</a>
  <div class="abs chip white">
    <svg width="40" height="40" viewBox="0 0 40 40" fill="none" stroke="#0c4f96" stroke-width="2"><rect x="4" y="4" width="22" height="32" rx="2"/><circle cx="30" cy="14" r="6"/><path d="M8 12h12M8 18h12M8 24h8"/></svg>
    <span>Quick Payment<br>Process</span>
  </div>
  <div class="abs chip purple">
    <svg width="40" height="40" viewBox="0 0 40 40" fill="none" stroke="#fff" stroke-width="2"><rect x="6" y="6" width="20" height="30" rx="2"/><path d="M10 12h12M10 18h4M16 18h4M10 24h4M16 24h4"/><rect x="24" y="24" width="12" height="8"/></svg>
    <span>No Prepayment<br>Fees</span>
  </div>
</section>

<section class="abs about">
  <div class="eyebrow">About Us</div>
  <h2>Our Loans will Fill Your<br>Dreams Come True</h2>
  <p class="lead">There are many variations of passages of lorem ipsum available the majority have suffered alteration in some form by injected humour.</p>
  <div class="badge" style="left:113px">
    <div class="ring"><svg width="36" height="36" viewBox="0 0 36 36" fill="none" stroke="#0c4f96" stroke-width="2"><circle cx="18" cy="15" r="10"/><path d="M18 9l2 4 4 .5-3 3 1 4-4-2-4 2 1-4-3-3 4-.5z"/><path d="M12 24l-3 9 5-2 3 3M24 24l3 9-5-2-3 3"/></svg></div>
    <div><b>Award Winning</b><small>Finance categories winning more than 10 awards</small></div>
  </div>
  <div class="badge" style="left:330px">
    <div class="ring"><svg width="36" height="36" viewBox="0 0 36 36" fill="none" stroke="#0c4f96" stroke-width="2"><rect x="6" y="5" width="20" height="26" rx="2"/><path d="M10 11h12M10 16h12M10 21h6"/><circle cx="26" cy="25" r="5"/></svg></div>
    <div><b>Certified Company</b><small>Approved Finance company to provide loans</small></div>
  </div>
  <div class="abs about-frame"></div>
  <div class="abs about-photo" role="img" aria-label="Photo of two advisers reviewing loan documents at a laptop"></div>
</section>

<section class="abs services">
  <div class="eyebrow light">What We're Offering</div>
  <h2>All Loans Services</h2>
</section>
<article class="abs loan-card" style="left:125px">
  <div class="img" role="img" aria-label="Photo of a couple shaking hands with a home loan adviser" style="background:linear-gradient(135deg,#e9e6df,#9fa3a6 60%,#5b6470)"></div>
  <h3>Home Loan</h3>
  <p>Home Loan provide low interest many variations of passages of lorem ipsum available the majority have some.</p>
  <a class="btn">Apply Loan</a>
</article>
<article class="abs loan-card" style="left:458px">
  <div class="img" role="img" aria-label="Photo of a businesswoman shaking hands in an office" style="background:linear-gradient(135deg,#5d6f86,#c9b79c 55%,#3d4c5d)"></div>
  <h3>Business Loan</h3>
  <p>Business Loan provide low interest many variations of passages of lorem ipsum available the majority have some.</p>
  <a class="btn" style="left:77px">Apply Loan</a>
</article>
<article class="abs loan-card" style="left:790px">
  <div class="img" role="img" aria-label="Photo of crop rows on a farm with a tractor" style="background:linear-gradient(180deg,#dbe5ea 0%,#c8d3d0 35%,#5b7f3a 45%,#2f5321 100%)"></div>
  <h3>Agriculture Loan</h3>
  <p>Agri Loan provide low interest many variations of passages of lorem ipsum available the majority have some.</p>
  <a class="btn">Apply Loan</a>
</article>

<section class="know">
  <div class="eyebrow">Get to Know About</div>
  <h2 class="abs">Flexible and Quick Business<br>Loans For You</h2>
  <div class="abs feature" style="left:124px">
    <svg width="44" height="44" viewBox="0 0 44 44" fill="none" stroke="#0c4f96" stroke-width="2"><circle cx="20" cy="22" r="14"/><path d="M14 28l12-12M15 17h1M25 27h1"/><path d="M32 30l6 6"/></svg>
    <span>Very Low Rates on All<br>Loans</span></div>
  <div class="abs feature" style="left:454px">
    <svg width="44" height="44" viewBox="0 0 44 44" fill="none" stroke="#0c4f96" stroke-width="2"><circle cx="24" cy="16" r="10"/><path d="M19 16l4 4 6-7"/><path d="M4 34h10l8 4 16-8"/></svg>
    <span>99.9% Success<br>Rate Guarantee</span></div>
  <div class="abs feature" style="left:790px">
    <svg width="44" height="44" viewBox="0 0 44 44" fill="none" stroke="#0c4f96" stroke-width="2"><path d="M22 4v20M12 10l20 8M32 10l-20 8"/><path d="M4 34h10l8 4 16-8"/></svg>
    <span>Flexible with Your<br>Repayments</span></div>
</section>

<section class="abs trust">
  <div class="eyebrow light">Trusted Company</div>
  <h2>Most of the People<br>Trust on Us For Fast<br>Services</h2>
  <ul class="checks">
    <li><svg width="20" height="20" viewBox="0 0 20 20" fill="none" stroke="#fff" stroke-width="2"><circle cx="10" cy="10" r="8"/><path d="M6 10l3 3 8-8"/></svg>Personal Loan</li>
    <li><svg width="20" height="20" viewBox="0 0 20 20" fill="none" stroke="#fff" stroke-width="2"><circle cx="10" cy="10" r="8"/><path d="M6 10l3 3 8-8"/></svg>Auto Loan</li>
    <li><svg width="20" height="20" viewBox="0 0 20 20" fill="none" stroke="#fff" stroke-width="2"><circle cx="10" cy="10" r="8"/><path d="M6 10l3 3 8-8"/></svg>Home Loan</li>
    <li><svg width="20" height="20" viewBox="0 0 20 20" fill="none" stroke="#fff" stroke-width="2"><circle cx="10" cy="10" r="8"/><path d="M6 10l3 3 8-8"/></svg>Education Loan</li>
    <li><svg width="20" height="20" viewBox="0 0 20 20" fill="none" stroke="#fff" stroke-width="2"><circle cx="10" cy="10" r="8"/><path d="M6 10l3 3 8-8"/></svg>Car Loan</li>
    <li><svg width="20" height="20" viewBox="0 0 20 20" fill="none" stroke="#fff" stroke-width="2"><circle cx="10" cy="10" r="8"/><path d="M6 10l3 3 8-8"/></svg>Wedding Loan</li>
  </ul>
</section>
<div class="abs steps">
  <div class="step"><span class="num">1</span><span>Easy loan solutions for small agency,<br>business and companies</span></div>
  <div class="step"><span class="num">2</span><span>Submit Required Document and Details<br>for loan approval</span></div>
  <div class="step"><span class="num">3</span><span>Take our loans now and pay later when<br>studies completed</span></div>
  <div class="step"><span class="num">4</span><span>Get small loans for more needs in 2 hours<br>with less documents</span></div>
</div>

<section class="abs why">
  <div class="abs why-photo" role="img" aria-label="Photo of a loan adviser signing paperwork with a client"></div>
  <div class="eyebrow">Our Benefits</div>
  <h2>Why Choose Us?</h2>
  <p class="lead">Provide your best loan services and our experience staff help you. Less document and fast approve process of passages.</p>
  <div class="badge" style="left:610px">
    <div class="ring"><svg width="36" height="36" viewBox="0 0 36 36" fill="none" stroke="#0c4f96" stroke-width="2"><circle cx="18" cy="12" r="4"/><circle cx="8" cy="14" r="3"/><circle cx="28" cy="14" r="3"/><path d="M11 28c0-5 3-8 7-8s7 3 7 8M3 26c0-4 2-6 5-6M33 26c0-4-2-6-5-6"/></svg></div>
    <div><b>Professional<br>Team</b></div>
  </div>
  <div class="badge" style="left:864px">
    <div class="ring"><svg width="36" height="36" viewBox="0 0 36 36" fill="none" stroke="#0c4f96" stroke-width="2"><rect x="8" y="6" width="22" height="24" rx="2"/><path d="M12 12h14M12 17h14M12 22h8M4 14h6M4 20h6"/></svg></div>
    <div><b>Quick<br>Payments</b></div>
  </div>
  <div class="bar" style="top:360px"><div class="label">Loan Process<small>90%</small></div><div class="track"><div class="fill" style="width:90%"></div></div></div>
  <div class="bar" style="top:428px"><div class="label">Consultancy<small>80%</small></div><div class="track"><div class="fill" style="width:80%"></div></div></div>
  <div class="bar" style="top:496px"><div class="label">Payment Benefits<small>85%</small></div><div class="track"><div class="fill" style="width:85%"></div></div></div>
</section>

<section class="abs cta">
  <p>Simple&nbsp; / &nbsp;Transparent&nbsp; / &nbsp;Secure</p>
  <h2>Get a Business Loans Quickly</h2>
  <a class="btn">Apply For Loan</a>
</section>

<footer class="abs footer">
  <div class="f-logo"><span class="mark"></span>Vantora</div>
  <p class="f-about">There are many variations of passages of lorem ipsum available the majority have suffered alteration in some form by injected humour.</p>
  <div class="abs f-col" style="left:404px;top:80px">
    <h4>Explore</h4>
    <ul class="f-links">
      <li>⟶ About Us</li><li>⟶ FAQ</li><li>⟶ Contact Us</li><li>⟶ Latest News</li><li>⟶ Loan Calculator</li>
    </ul>
  </div>
  <div class="abs f-col" style="left:569px;top:80px">
    <h4>Latest News</h4>
    <div class="news"><div class="thumb" role="img" aria-label="Photo of an office meeting"></div><div><small>31 December,2024</small><span>Lorem Ipsum is simply dummy text of the printing</span></div></div>
    <div class="news" style="border:none"><div class="thumb" role="img" aria-label="Photo of a client consultation"></div><div><small>23 December,2024</small><span>Lorem Ipsum is simply dummy text of the printing</span></div></div>
  </div>
  <div class="abs f-col" style="left:872px;top:82px">
    <h4>Get In Touch</h4>
    <div class="contact-item"><svg width="20" height="14" viewBox="0 0 20 14"><rect x="1" y="1" width="18" height="12" fill="none" stroke="#fff" stroke-width="2"/><path d="M1 1l9 7 9-7" fill="none" stroke="#fff" stroke-width="2"/></svg><span>Mail<br>hello@vantora.example</span></div>
    <div class="contact-item"><svg width="16" height="16" viewBox="0 0 24 24"><path d="M6 2l4 4-2 3c1 3 4 6 7 7l3-2 4 4-3 4C10 21 3 14 2 5z" fill="#fff"/></svg><span>(02) 5550 1846<br>(02) 5550 1847 (fax)</span></div>
    <div class="contact-item"><svg width="16" height="20" viewBox="0 0 16 20"><path d="M8 1a7 7 0 0 1 7 7c0 5-7 11-7 11S1 13 1 8a7 7 0 0 1 7-7z" fill="none" stroke="#fff" stroke-width="2"/><circle cx="8" cy="8" r="2.5" fill="#fff"/></svg><span style="font-size:13px">Lorem Ipsum is simply dummy<br>text of the printing</span></div>
  </div>
  <div class="copyright">Copyright © 2025.hello@vantora.example.All Rights Reserved</div>
</footer>

</body>
</html>
```